Modern Business Card

Modern professional business card with more than just logo and demographic info. Something memorable.

We are a trendy/modern chiropractic group with an emphasis on neurology, hence the minimalist-type brain logo. We want to convey that modern and technical aspect with professionalism and the elite nature of our practice environment.

```html
<!DOCTYPE html>
<html lang="en">
<head>
<meta charset="utf-8">
<title>Meridian Chiropractic – Business Card</title>
<link rel="stylesheet" href="https://fonts.googleapis.com/css2?family=Lato:ital,wght@0,400;0,700;0,900;1,400&display=swap">
<style>
  :root {
    --stage: #2a2a2a;
    --brand-blue: #4a80c2;
    --ink: #1c2230;
    --body-grey: #333a44;
    --muted-grey: #5a5a5a;
    --rule-blue: #8fb2dd;
    --paper: #ffffff;
  }
  * { box-sizing: border-box; margin: 0; padding: 0; }
  html, body {
    width: 1200px; height: 878px; overflow: hidden;
    background: var(--stage);
    font-family: "Lato", Arial, sans-serif;
  }
  .canvas { position: relative; width: 1200px; height: 878px; }

  .card {
    position: absolute; left: 290px; width: 620px; height: 354px;
    box-shadow: 0 10px 30px rgba(0,0,0,.45);
    overflow: hidden;
  }
  .card--front { top: 45px; background: var(--brand-blue); }
  .card--back  { top: 479px; background: var(--paper); }

  /* Wordmark */
  .wordmark { display: flex; align-items: center; gap: 16px; color: var(--ink); font-weight: 700; }
  .wordmark__square { width: 40px; height: 40px; flex: none; }
  .wordmark__text { display: flex; flex-direction: column; line-height: 1; letter-spacing: .04em; }
  .wordmark__main { font-size: 40px; }
  .wordmark__sub  { font-size: 21px; margin-top: 4px; letter-spacing: .07em; }

  .card--front .wordmark {
    position: absolute; left: 50%; top: 50%; transform: translate(-50%, -50%);
  }
  .card--front .wordmark__square { background: var(--paper); }

  .card--back .wordmark { position: absolute; right: 44px; top: 148px; }
  .card--back .wordmark__square { background: var(--brand-blue); }
  .card--back .wordmark__main { font-size: 34px; }
  .card--back .wordmark__sub  { font-size: 18px; }

  /* Identity */
  .identity { position: absolute; left: 40px; top: 34px; }
  .identity__name { color: var(--brand-blue); font-weight: 900; font-size: 27px; letter-spacing: .01em; }
  .identity__role { color: var(--body-grey); font-style: italic; font-size: 16px; margin-top: 2px; }

  /* Contact */
  .contact { position: absolute; left: 36px; top: 196px; list-style: none; }
  .contact__item { display: flex; align-items: center; gap: 12px; font-size: 17px; color: var(--body-grey); height: 26px; }
  .contact__icon { width: 16px; height: 16px; flex: none; fill: var(--brand-blue); }

  .address { position: absolute; left: 28px; top: 290px; display: flex; align-items: center; gap: 12px; font-size: 17px; color: var(--body-grey); }
  .address__rule { position: absolute; left: 28px; right: 34px; top: 284px; height: 1px; background: var(--rule-blue); }

  .band { position: absolute; bottom: 0; left: 0; right: 0; height: 22px; }
  .band__accent { position: absolute; left: 0; bottom: 0; width: 40px; height: 22px; background: var(--muted-grey); }
  .band__bar { position: absolute; left: 46px; right: 0; bottom: 0; height: 16px; background: var(--brand-blue); }
</style>
</head>
<body>
<main class="canvas">

  <section class="card card--front" aria-label="Card front">
    <div class="wordmark">
      <span class="wordmark__square"></span>
      <span class="wordmark__text">
        <span class="wordmark__main">MERIDIAN</span>
        <span class="wordmark__sub">CHIROPRACTIC</span>
      </span>
    </div>
  </section>

  <section class="card card--back" aria-label="Card back">
    <div class="identity">
      <h1 class="identity__name">JOHN SMITH</h1>
      <p class="identity__role">Founder &amp; CEO</p>
    </div>

    <div class="wordmark">
      <span class="wordmark__square"></span>
      <span class="wordmark__text">
        <span class="wordmark__main">MERIDIAN</span>
        <span class="wordmark__sub">CHIROPRACTIC</span>
      </span>
    </div>

    <ul class="contact">
      <li class="contact__item">
        <svg class="contact__icon" viewBox="0 0 24 24" aria-hidden="true"><path d="M6.6 10.8a15.1 15.1 0 0 0 6.6 6.6l2.2-2.2a1 1 0 0 1 1-.25 11.4 11.4 0 0 0 3.6.57 1 1 0 0 1 1 1V20a1 1 0 0 1-1 1A17 17 0 0 1 3 4a1 1 0 0 1 1-1h3.5a1 1 0 0 1 1 1c0 1.25.2 2.45.57 3.57a1 1 0 0 1-.25 1z"/></svg>
        1234567890
      </li>
      <li class="contact__item">
        <svg class="contact__icon" viewBox="0 0 24 24" aria-hidden="true"><path d="M2 5h20v14H2zm2 2v.5l8 5 8-5V7l-8 5z"/></svg>
        info@yourmail.com
      </li>
      <li class="contact__item">
        <svg class="contact__icon" viewBox="0 0 24 24" aria-hidden="true"><path d="M12 2a10 10 0 1 0 0 20 10 10 0 0 0 0-20zm0 2c.9 0 2.2 2 2.7 5H9.3C9.8 6 11.1 4 12 4zM4.3 11h3a17 17 0 0 0 0 2h-3a8 8 0 0 1 0-2zm5 0h5.4a15 15 0 0 1 0 2H9.3a15 15 0 0 1 0-2zm7.4 0h3a8 8 0 0 1 0 2h-3a17 17 0 0 0 0-2zM9.3 15h5.4c-.5 3-1.8 5-2.7 5s-2.2-2-2.7-5z"/></svg>
        www.yourwebsite.com
      </li>
    </ul>

    <div class="address__rule"></div>
    <p class="address">
      <svg class="contact__icon" viewBox="0 0 24 24" aria-hidden="true"><path d="M12 2a7 7 0 0 0-7 7c0 5 7 13 7 13s7-8 7-13a7 7 0 0 0-7-7zm0 9.5A2.5 2.5 0 1 1 12 6.5a2.5 2.5 0 0 1 0 5z"/></svg>
      1234 First Line Address 5678 Second Line Address
    </p>

    <div class="band">
      <span class="band__accent"></span>
      <span class="band__bar"></span>
    </div>
  </section>

</main>
</body>
</html>
```